Broschüre für Hersteller von Vendingautomaten
Zielgruppe
Unser Unternehmen ist ein Start-up im Bereich Vendingautomaten.
Wir stellen Verkaufsautomaten im öffentlichen Raum auf für Snacks, Getränke und Secret Packs.
Unsere Zielgruppe ist nicht genau zu definieren, aber primär Kinder bis Ende 50.
Aufgabenstellung
Bei dem Projekt geht es um eine Broschüre, um uns bei Kunden wie Privatpersonen aber auch Gemeinden und Städte, bekannt zu machen und uns zu präsentieren, damit diese wissen, mit wem sie es zu tun haben.

```html
<!DOCTYPE html>
<html lang="de">
<head>
<meta charset="UTF-8">
<title>Broschüre – Verkaufsautomat Standard</title>
<link href="https://fonts.googleapis.com/css2?family=Oswald:wght@400;600&family=Roboto:wght@400;500;700&display=swap" rel="stylesheet">
<style>
  :root {
    --backdrop: #e4e4e4;
    --navy-deep: #0c1228;
    --navy: #18203f;
    --navy-light: #232c52;
    --orange: #f07a1a;
    --white: #ffffff;
    --text-dim: #d7dbe8;
    --rule: rgba(255,255,255,0.14);
  }
  * { margin: 0; padding: 0; box-sizing: border-box; }
  html, body { width: 1200px; height: 1200px; overflow: hidden; }
  body {
    background: var(--backdrop);
    font-family: "Roboto", Arial, sans-serif;
    position: relative;
  }
  .spread {
    position: absolute;
    left: 40px; top: 270px;
    width: 1120px; height: 660px;
    display: flex;
    box-shadow: 0 10px 30px rgba(0,0,0,0.25);
  }
  .page {
    position: relative;
    width: 560px; height: 660px;
    background: linear-gradient(160deg, var(--navy) 0%, var(--navy-deep) 100%);
    color: var(--white);
    overflow: hidden;
  }
  .page--left { background: linear-gradient(200deg, var(--navy-light) 0%, var(--navy-deep) 80%); }

  /* left page */
  .product-title {
    position: absolute; left: 50px; top: 92px;
    font-family: "Oswald", Arial, sans-serif;
    line-height: 1.05;
    letter-spacing: 0.5px;
  }
  .product-title__line { display: block; font-size: 38px; font-weight: 400; color: var(--white); }
  .product-title__line--accent { font-weight: 600; color: var(--orange); }
  .feature-list {
    position: absolute; left: 50px; top: 210px; width: 205px;
    list-style: none;
    font-size: 10.5px; line-height: 1.45;
    color: var(--text-dim);
  }
  .feature-list li { position: relative; padding-left: 12px; margin-bottom: 10px; }
  .feature-list li::before {
    content: ""; position: absolute; left: 0; top: 6px;
    width: 4px; height: 4px; border-radius: 50%; background: var(--white);
  }
  .accent-dot {
    position: absolute; left: 278px; top: 186px;
    width: 90px; height: 90px; border-radius: 50%;
    background: var(--orange);
  }
  .machine-visual {
    position: absolute; left: 318px; top: 180px;
    width: 165px; height: 318px;
    background: linear-gradient(180deg, #d9dde3 0%, #9aa0a8 55%, #2a2d33 100%);
    border-radius: 3px;
  }

  /* right page */
  .spec-table {
    position: absolute; left: 20px; top: 110px; width: 488px;
    border-collapse: collapse;
    font-size: 9.5px;
    color: var(--text-dim);
  }
  .spec-table th {
    background: var(--orange); color: var(--white);
    text-align: left; font-weight: 700;
    padding: 3px 8px; font-size: 10px;
  }
  .spec-table td {
    padding: 2.5px 8px;
    border-bottom: 1px solid var(--rule);
    height: 16.5px;
  }
  .spec-table td.spec-label { width: 44%; }
  .spec-table td.spec-value { color: var(--white); }

  .accessory-block {
    position: absolute; left: 20px; top: 478px; width: 488px;
    display: flex;
  }
  .accessory-block__tag {
    width: 18px; background: var(--orange);
    display: flex; align-items: center; justify-content: center;
  }
  .accessory-block__tag span {
    transform: rotate(-90deg);
    font-size: 9.5px; font-weight: 700; color: var(--white);
    white-space: nowrap;
  }
  .accessory-table { flex: 1; border-collapse: collapse; font-size: 9.5px; color: var(--text-dim); }
  .accessory-table td { padding: 2.5px 8px; border-bottom: 1px solid var(--rule); height: 16.5px; }
  .accessory-table td.spec-label { width: 41%; }
  .accessory-table td.spec-value { color: var(--white); }

  .extras {
    position: absolute; left: 20px; top: 570px; width: 488px;
    display: flex; gap: 22px;
  }
  .extra-item { display: flex; align-items: flex-start; gap: 8px; flex: 1; }
  .extra-item__label {
    background: var(--orange); color: var(--white);
    font-size: 9.5px; font-weight: 700; line-height: 1.2;
    padding: 3px 7px;
  }
  .extra-item__label--wrap { width: 108px; }
  .extra-item__text { font-size: 8px; line-height: 1.35; color: var(--text-dim); }
</style>
</head>
<body>
  <main class="spread">
    <section class="page page--left">
      <h1 class="product-title">
        <span class="product-title__line">VERKAUFSAUTOMAT</span>
        <span class="product-title__line product-title__line--accent">STANDARD</span>
      </h1>
      <ul class="feature-list">
        <li>Mit 24-Stunden-Automatenverkauf bietest du deinen Kunden enorme Bequemlichkeit.</li>
        <li>Du kannst eine breite Palette an Produkten in diesen Automaten anbieten, die rund um die Uhr zugänglich sind.</li>
        <li>Dank Cloud-Technologie behältst du immer einen genauen Überblick über deinen Warenbestand.</li>
        <li>Analysiere, welche Artikel am besten ankommen, plane Sonderaktionen oder schalte Werbevideos. Diese Automaten sind mit modernster Technologie ausgestattet, um deinen Kunden</li>
        <li>ein hervorragendes Serviceerlebnis und ein innovatives Einkaufserlebnis zu bieten. Der Einsatzbereich des „Standard“ Verkaufsautomaten</li>
        <li>ist vielseitig und kann individuell angepasst werden.</li>
      </ul>
      <div class="accent-dot"></div>
      <div class="machine-visual" role="img" aria-label="Foto des Verkaufsautomaten Standard mit Glasfront und gefüllten Spiralfächern"></div>
    </section>

    <section class="page page--right">
      <table class="spec-table">
        <thead><tr><th colspan="2">Technische Daten</th></tr></thead>
        <tbody>
          <tr><td class="spec-label">Gesamtmaße (BxHxT)</td><td class="spec-value">1045 x 1940 x 930 mm</td></tr>
          <tr><td class="spec-label">Gewicht</td><td class="spec-value">300 kg</td></tr>
          <tr><td class="spec-label">Nennspannung</td><td class="spec-value">230 V AC / 50Hz</td></tr>
          <tr><td class="spec-label">Nennstrom</td><td class="spec-value">4,5 A</td></tr>
          <tr><td class="spec-label">Nennleistung</td><td class="spec-value">1035 VA</td></tr>
          <tr><td class="spec-label">Anschlußart</td><td class="spec-value">1 Ph / N / PE</td></tr>
          <tr><td class="spec-label">Zertifizierung</td><td class="spec-value">CE</td></tr>
          <tr><td class="spec-label">IP-Schutzart</td><td class="spec-value">IP20</td></tr>
          <tr><td class="spec-label">Umgebungstemperatur</td><td class="spec-value">-10 °C – +40 °C</td></tr>
          <tr><td class="spec-label">Temperatur Warenverkaufsraum</td><td class="spec-value">+4 °C – +25 °C</td></tr>
          <tr><td class="spec-label">Kältemittel</td><td class="spec-value">R 1234yf</td></tr>
          <tr><td class="spec-label">Fächeranzahl</td><td class="spec-value">260</td></tr>
          <tr><td class="spec-label">Anzahl Tablare</td><td class="spec-value">6</td></tr>
          <tr><td class="spec-label">Anzahl Förderspiralen pro Tablar</td><td class="spec-value">7</td></tr>
          <tr><td class="spec-label">Ausgabetechnik</td><td class="spec-value">Dose- und Spiralförderer / Produktlift / Ausgabeklappe</td></tr>
          <tr><td class="spec-label">Automatenschnittstelle Zahlungsmittel</td><td class="spec-value">MDB-Bus</td></tr>
          <tr><td class="spec-label">Zahlungsmittel</td><td class="spec-value">Bargeldzahlung (Münze und Banknote)</td></tr>
          <tr><td class="spec-label">Touch-Display</td><td class="spec-value">7" (kapazitiv)</td></tr>
          <tr><td class="spec-label">Betriebssystem</td><td class="spec-value">Fenstra OS 10</td></tr>
          <tr><td class="spec-label">Gewährleistung</td><td class="spec-value">1 Jahr</td></tr>
        </tbody>
      </table>

      <div class="accessory-block">
        <div class="accessory-block__tag"><span>Zubehör</span></div>
        <table class="accessory-table">
          <tr><td class="spec-label">Kartenzahlungsterminal Debitkarte</td><td class="spec-value">Kontaktlos- und Kontaktkartenterminal sowie Debit- und Kreditkarte</td></tr>
          <tr><td class="spec-label">Altersverifikation</td><td class="spec-value">Ausweislesegerät</td></tr>
          <tr><td class="spec-label">Vandalismusschutz</td><td class="spec-value">Schlagschutzfolie, -schelle, -gitter, Wand- / Bodenbefestigung</td></tr>
          <tr><td class="spec-label">UV-Schutzfolie</td><td class="spec-value"></td></tr>
        </table>
      </div>

      <div class="extras">
        <div class="extra-item">
          <span class="extra-item__label">Sonderzubehör</span>
          <span class="extra-item__text">Individuelle Seitenfolierung, LED-Beleuchtung, Produktfolierung</span>
        </div>
        <div class="extra-item">
          <span class="extra-item__label extra-item__label--wrap">Erweiterungs&shy;möglichkeiten</span>
          <span class="extra-item__text">Getränke-Automat, Kombi-Automat mit Kühlfach</span>
        </div>
      </div>
    </section>
  </main>
</body>
</html>
```